Bref créative
brook gate realty business card
Simple
Miles Vetcher
Licensed Real Estate Broker
2385 West 9th Avenue
Brooklyn, NY 11230
brookgaterealtyny@quorvana.com
www.bgrny.com
front should be standard and simple
the logo in a corner and small or in the back ground.
logo with a clean black or white setting. possibly with borders
i want the card to portray power and elegance.
i uploaded the complete zip file from tavelink if this is to much please tell me and ill changeit.

```html
<!DOCTYPE html>
<html lang="en">
<head>
<meta charset="utf-8">
<title>Brook Gate Realty – Stationery</title>
<link rel="stylesheet" href="https://fonts.googleapis.com/css2?family=Cinzel:wght@500&family=Open+Sans:wght@400;600&display=swap">
<style>
  :root {
    --stage: #3b2a21;
    --paper: #ffffff;
    --ink: #4a4a4a;
    --ink-soft: #8a8a8a;
    --faint: #efefef;
    --flap: #7a7a7a;
    --flap-light: #d9d9d9;
    --shadow: rgba(0,0,0,.35);
  }
  * { margin: 0; padding: 0; box-sizing: border-box; }
  html, body { width: 1200px; height: 456px; overflow: hidden; }
  body { background: var(--stage); font-family: "Open Sans", sans-serif; color: var(--ink); position: relative; }

  .sheet { position: absolute; background: var(--paper); box-shadow: 0 3px 8px var(--shadow); overflow: hidden; }

  .brand { font-family: "Cinzel", serif; font-weight: 500; color: var(--ink); text-transform: uppercase; letter-spacing: .06em; display: flex; align-items: center; gap: 5px; white-space: nowrap; position: absolute; z-index: 1; }
  .brand-mark { width: 8px; height: 8px; background: var(--ink); flex: none; }

  .watermark { position: absolute; font-family: "Cinzel", serif; font-weight: 500; color: var(--faint); text-transform: uppercase; line-height: .95; letter-spacing: .02em; z-index: 0; }

  /* business cards */
  .card-front { left: 62px; top: 108px; width: 197px; height: 115px; }
  .card-front .brand { left: 0; right: 0; top: 14px; justify-content: center; font-size: 7px; }
  .card-front .person { position: absolute; left: 0; right: 0; top: 36px; text-align: center; }
  .person-name { font-size: 5.5px; font-weight: 600; }
  .person-title { font-size: 4.5px; color: var(--ink-soft); margin-top: 1px; }
  .card-front .details { position: absolute; left: 14px; top: 64px; font-size: 4.5px; line-height: 1.6; }
  .card-front .contact { position: absolute; left: 112px; top: 64px; font-size: 4.5px; line-height: 1.6; }

  .card-back { left: 62px; top: 235px; width: 197px; height: 115px; }
  .card-back .brand { left: 0; right: 0; top: 36px; justify-content: center; font-size: 9px; }
  .card-back .web { position: absolute; left: 0; right: 0; top: 90px; text-align: center; font-size: 5px; color: var(--ink-soft); }

  /* letterheads */
  .letterhead { top: 43px; width: 260px; height: 358px; }
  .letterhead-a { left: 294px; }
  .letterhead-b { left: 586px; }
  .letterhead .brand { font-size: 7px; top: 18px; }
  .letterhead-a .brand { left: 16px; }
  .letterhead-b .brand { left: 0; right: 0; justify-content: center; }
  .letterhead .watermark { left: 24px; top: 80px; font-size: 44px; }
  .letterhead-b .watermark { left: 30px; }
  .letterhead .header-lines { position: absolute; left: 150px; top: 16px; font-size: 4px; line-height: 1.6; color: var(--ink-soft); }
  .letterhead .footer-line { position: absolute; left: 0; right: 0; bottom: 22px; text-align: center; font-size: 4px; color: var(--ink-soft); }

  /* envelopes */
  .envelope { left: 883px; width: 245px; }
  .env-back-a { top: 43px; height: 90px; }
  .env-front-a { top: 128px; height: 74px; }
  .env-back-b { top: 212px; height: 76px; }
  .env-front-b { top: 283px; height: 120px; }
  .envelope svg { display: block; width: 100%; height: 100%; }
  .env-front-a .brand { left: 0; right: 0; justify-content: center; top: 32px; font-size: 7px; }
  .env-front-b .brand { left: 12px; top: 12px; font-size: 6px; }
  .env-front-b .watermark { left: 120px; top: 40px; font-size: 24px; }
</style>
</head>
<body>

  <section class="sheet card-front">
    <div class="brand"><span class="brand-mark"></span>brook gate realty</div>
    <div class="person">
      <p class="person-name">Miles Vetcher</p>
      <p class="person-title">Licensed Real Estate Broker</p>
    </div>
    <div class="details">
      <p>2385 West 9th Avenue</p>
      <p>Brooklyn, NY 11230</p>
    </div>
    <div class="contact">
      <p>(718) 555-0142</p>
      <p>www.bgrny.com</p>
      <p>brookgaterealtyny@quorvana.com</p>
    </div>
  </section>

  <section class="sheet card-back">
    <div class="brand"><span class="brand-mark"></span>brook gate realty</div>
    <p class="web">www.bgrny.com</p>
  </section>

  <section class="sheet letterhead letterhead-a">
    <div class="brand"><span class="brand-mark"></span>brook gate realty</div>
    <div class="header-lines">
      <p>(718) 555-0142 · 2385 West 9th Avenue</p>
      <p>(718) 555-0143 · Brooklyn, NY 11230</p>
    </div>
    <p class="watermark" aria-hidden="true">brook<br>gate<br>realty</p>
  </section>

  <section class="sheet letterhead letterhead-b">
    <div class="brand"><span class="brand-mark"></span>brook gate realty</div>
    <p class="watermark" aria-hidden="true">brook<br>gate<br>realty</p>
    <p class="footer-line">2385 West 9th Avenue, Brooklyn, NY 11230 · (718) 555-0142 · www.bgrny.com · brookgaterealtyny@quorvana.com</p>
  </section>

  <section class="sheet envelope env-back-a">
    <svg viewBox="0 0 245 90" preserveAspectRatio="none">
      <rect width="245" height="90" fill="var(--paper)"/>
      <polygon points="0,0 245,0 122,68" fill="var(--flap)"/>
    </svg>
  </section>

  <section class="sheet envelope env-front-a">
    <div class="brand"><span class="brand-mark"></span>brook gate realty</div>
  </section>

  <section class="sheet envelope env-back-b">
    <svg viewBox="0 0 245 76" preserveAspectRatio="none">
      <rect width="245" height="76" fill="var(--paper)"/>
      <polygon points="0,0 245,0 122,58" fill="var(--flap)"/>
    </svg>
  </section>

  <section class="sheet envelope env-front-b">
    <div class="brand"><span class="brand-mark"></span>brook gate realty</div>
    <p class="watermark" aria-hidden="true">brook<br>gate<br>realty</p>
  </section>

</body>
</html>
```